High End Notary Service Business Card Design

Want a professional and elegant/luxurious business card that is clean and simple in the design. A notary is a trusted professional that helps people sign very important documents. The card should be in alignment with this service provided.

Most of the time, service will be for the purchase of a home or refinance of a mortgage

There is NO LOGO. This is aesthetic. A look and feel. Conveying professionalism and concierge level of service.

Target Market(s)

Other business professionals, Lawyers, Escrow Officers, Loan Officers

Industry/Entity Type

Legal

Contact Information for Business Card

This will be a one-sided business card

Colors
35a7d7
3176b5
85cae6
d3a5cc
b868aa
ffffff
0356a4

Requirements
Must have
• Lorena T. Mirabel-Hodgkins
Notary Public

642-871-3094
MirabelSigningDesk@Wexmail.com
Nice to have
• Headshot photo below. Convey the aspect of signing documents. No black cards. Preference is shades of blue: light blue, navy, aqua, gold, white, or lavendar, etc.
Should not have
• No scales or legal scales.

```html
<!DOCTYPE html>
<html lang="en">
<head>
<meta charset="utf-8">
<title>Notary Public Business Card</title>
<link href="https://fonts.googleapis.com/css2?family=Jost:wght@400&display=swap" rel="stylesheet">
<style>
  :root {
    --page-bg: #f3f3f3;
    --card-navy: #1c2946;
    --deep-navy: #16213b;
    --gold: #d4b47e;
  }
  html, body {
    margin: 0;
    padding: 0;
    width: 1200px;
    height: 1200px;
    overflow: hidden;
    background: var(--page-bg);
  }
  .business-card {
    position: absolute;
    left: 224px;
    top: 385px;
    width: 751px;
    height: 428px;
    background: var(--card-navy);
    overflow: hidden;
    font-family: "Jost", sans-serif;
    color: var(--gold);
  }
  .backdrop-emblem {
    position: absolute;
    left: 0;
    top: 0;
    width: 751px;
    height: 428px;
  }
  .identity {
    position: absolute;
    right: 62px;
    top: 194px;
    text-align: right;
  }
  .name-line {
    display: flex;
    align-items: center;
    justify-content: flex-end;
    gap: 8px;
    font-size: 30px;
    letter-spacing: 0.3px;
    line-height: 1;
  }
  .quill-mark {
    display: block;
    width: 30px;
    height: 92px;
  }
  .role-title {
    margin-top: -16px;
    font-size: 22px;
    letter-spacing: 0.4px;
  }
  .contact-list {
    position: absolute;
    right: 56px;
    top: 318px;
    list-style: none;
    margin: 0;
    padding: 0;
  }
  .contact-item {
    display: flex;
    align-items: center;
    justify-content: flex-end;
    gap: 12px;
    height: 36px;
    font-size: 22px;
    letter-spacing: 0.3px;
  }
  .contact-icon {
    width: 30px;
    height: 30px;
    flex: none;
  }
</style>
</head>
<body>
  <section class="business-card">
    <svg class="backdrop-emblem" viewBox="0 0 751 428" aria-hidden="false">
      <path d="M 183 55 A 172 172 0 1 0 270 65" fill="none" stroke="var(--deep-navy)" stroke-width="9" stroke-linecap="round"/>
      <rect role="img" aria-label="Large faint quill feather decoration" x="176" y="30" width="62" height="370" rx="31" fill="var(--deep-navy)" transform="rotate(14 207 215)"/>
    </svg>

    <div class="identity">
      <div class="name-line">
        <span class="given-name">Lorena T.</span>
        <svg class="quill-mark" viewBox="0 0 30 92">
          <rect role="img" aria-label="Small gold quill feather accent" x="9" y="2" width="13" height="88" rx="6.5" fill="var(--gold)" transform="rotate(14 15 46)"/>
        </svg>
        <span class="family-name">Mirabel-Hodgkins</span>
      </div>
      <div class="role-title">Notary Public</div>
    </div>

    <ul class="contact-list">
      <li class="contact-item">
        <span class="contact-text">642 - 871 - 3094</span>
        <svg class="contact-icon" viewBox="0 0 30 30" aria-label="Phone">
          <circle cx="15" cy="15" r="13" fill="none" stroke="var(--gold)" stroke-width="2"/>
          <path d="M10.5 8.5 l2.5 -0.5 l1.5 3.5 l-1.8 1.3 q1.3 2.8 3.8 4 l1.4 -1.7 l3.4 1.6 l-0.5 2.5 q-6 1 -10.3 -10.7z" fill="none" stroke="var(--gold)" stroke-width="1.6" stroke-linejoin="round"/>
        </svg>
      </li>
      <li class="contact-item">
        <span class="contact-text">MirabelSigningDesk@Wexmail.com</span>
        <svg class="contact-icon" viewBox="0 0 30 30" aria-label="Email">
          <circle cx="15" cy="15" r="13" fill="none" stroke="var(--gold)" stroke-width="2"/>
          <rect x="8.5" y="10.5" width="13" height="9" rx="1.5" fill="none" stroke="var(--gold)" stroke-width="1.6"/>
          <path d="M9 11.5 l6 4.5 l6 -4.5" fill="none" stroke="var(--gold)" stroke-width="1.6" stroke-linejoin="round"/>
        </svg>
      </li>
    </ul>
  </section>
</body>
</html>
```